Test and Tag business card design

We are an appliance test and tag company in Brisbane Australia requiring a business card design.
I don't have a logo.
Card front: Matte black background with white font.
Card back: White background with black font colour
Examples are attached
Minimalist design
Reason: Looking for more designs with an extreme minimal feel
Industry/Entity Type
Appliance
Contact Information for Business Card
Business name: Harbor Check and Label
Description: Onsite Electrical Testing and Tagging
Licence No. 41853
Name: Greg Pellow
Mobile: 0418 526 937
Email: greg@harborcheckandlabel.com.au
Web: harborcheckandlabel.com.au
Logo Text
Harbor Check and Label
Look and feel

```html
<!DOCTYPE html>
<html lang="en">
<head>
<meta charset="utf-8">
<title>Harbor Check and Label – Business Card</title>
<link rel="stylesheet" href="https://fonts.googleapis.com/css2?family=Josefin+Sans:wght@300;400&display=swap">
<style>
  :root {
    --stage: #e9e7e4;
    --card-light: #ffffff;
    --card-dark: #0d0d0d;
    --ink-dark: #111111;
    --ink-light: #f2f2f2;
    --ink-muted: #cfcfcf;
    --divider: #4a4a4a;
  }
  * { margin: 0; padding: 0; box-sizing: border-box; }
  html, body {
    width: 1200px; height: 1000px; overflow: hidden;
    background: var(--stage);
    font-family: "Josefin Sans", sans-serif;
  }
  .canvas { position: relative; width: 1200px; height: 1000px; }

  .card { position: absolute; box-shadow: 0 4px 14px rgba(0,0,0,0.18); }

  .card--back {
    left: 79px; top: 31px; width: 603px; height: 345px;
    background: var(--card-light); color: var(--ink-dark);
  }
  .card--back .brand {
    position: absolute; left: 0; right: 0; top: 162px;
    text-align: center; font-size: 44px; font-weight: 400;
    letter-spacing: -1px; color: var(--ink-dark); white-space: nowrap;
  }
  .card--back .web {
    position: absolute; left: 0; right: 0; top: 314px;
    text-align: center; font-size: 15px; font-weight: 300;
  }

  .card--front {
    left: 565px; top: 397px; width: 610px; height: 348px;
    background: var(--card-dark); color: var(--ink-light);
  }
  .card--front .brand {
    position: absolute; left: 38px; width: 260px; top: 158px;
    font-size: 29px; font-weight: 400; letter-spacing: -0.5px;
    color: var(--ink-light); white-space: nowrap;
  }
  .card--front .divider {
    position: absolute; left: 321px; top: 110px; width: 1px; height: 140px;
    background: var(--divider);
  }
  .contact { position: absolute; left: 347px; top: 117px; }
  .contact .name { font-size: 24px; font-weight: 300; margin-bottom: 22px; }
  .contact .line {
    font-size: 15px; font-weight: 300; line-height: 24px;
    color: var(--ink-muted); white-space: nowrap;
  }
  .contact .line span { display: inline-block; width: 18px; }
  .card--front .tagline {
    position: absolute; left: 0; right: 0; top: 318px;
    text-align: center; font-size: 13px; font-weight: 300; color: var(--ink-muted);
  }
</style>
</head>
<body>
<main class="canvas">
  <section class="card card--back">
    <div class="brand">harborcheck&amp;label</div>
    <div class="web">www.harborcheckandlabel.com.au</div>
  </section>

  <section class="card card--front">
    <div class="brand">harborcheck&amp;label</div>
    <div class="divider"></div>
    <div class="contact">
      <div class="name">Greg Pellow</div>
      <div class="line"><span>m.</span>0418 526 937</div>
      <div class="line"><span>e.</span>greg@harborcheckandlabel.com.au</div>
      <div class="line"><span>w.</span>www.harborcheckandlabel.com.au</div>
    </div>
    <div class="tagline">Onsite Electrical Testing &amp; Tagging – Licence No. 41853</div>
  </section>
</main>
</body>
</html>
```